Tidewell Marketing company is looking for a web page design

Your projects should contain:

1. Header: Logo provided by us.
2. Top nav bar: offer, about us, experience, contact.
3. “Choose language” button.
4. Main section: panoramic picture (static, professional, modern).
5. Below section: 3 blocks (image+title+description), which represent our 3 main activities (titles):
• Market Research,
• Marketing Plans,
• Marketing Project.
6. ‘Contact us’ form – Message (text: “Write your message and give us details about your company and activities”), Email, SEND).
7. Page footer: (4 section: Contact, Social Media, Blog, Partners).
Updates

Hello!

I uploaded new file 'general_look', which is our idea how the page should generally look like.

BUT! it doesn't mean that your projects should look exactly like this project e.g.:
* titles Market Research, Marketing Plans, Marketing Project can be above these: Image 1,2,3.
* everything doesn't have to be in square and rectangle shape. You can try to manipulate with blocks and can add elipse elemnts or something similar.

We will appreciate your innovative ideas. Just wanted to give you general plan of the site and ilustrate all elements that we require.

Best Regards,
Benedek

IMPORTENT

Please remember that the main picture should be panoramic. Please do not close it in frame.

Target Market(s)

Small and middle sized companies, which would like to export their goods and services abroad and are interested in raising funds from Northgate Trade Council to expand their activities. These are rather industrial companies with low level of innovativeness. Our mission is to build image of the client’s company and increase awareness of their products to improve their competitiveness and innovativeness.

Industry/Entity Type

It Company

Requirements
Must have
• 1. Create designs of main page and subpage.
2. Subpage: Logo, Header, language button, place for article, navigation menu on the right side - below it “contact us” button , footer on the bottom. (In this section we are looking mainly for the design of the header and navigation menu).
3. The whole design should be a series of horizontal blocks.
4. Your projects should be associated with features such as: Reliability, Security, Professionalism, Openness, Uniqueness.
5. The design should be simple, fresh, readable, easy to use and should create a feeling of high quality services.
6. Possibility to change the panoramic picture (separate layer in a graphic file).
7. All pictures and blocks should be static, no movements.
8. Style of the page should be compliant with the logo design, font: Swiss.
9. Designs that we like: http://www.fernvale-studio.pl/, http://www.plumquarry.com/.
Should not have
• There shouldn’t be any distractions and not matching parts (whole design should be compact and easy to interpret and remember).

```html
<!DOCTYPE html>
<html lang="en">
<head>
<meta charset="utf-8">
<title>Tidewell Marketing</title>
<link rel="stylesheet" href="https://fonts.googleapis.com/css2?family=Source+Sans+3:ital,wght@0,400;0,600;0,700;1,400&display=swap">
<style>
:root{
  --navy:#0f4a78;
  --blue:#1f6aa0;
  --ink:#1e1e1e;
  --dark:#0d0d0f;
  --panel:#262626;
  --panel-text:#d4d4d4;
  --sky-top:#dfe8ef;
  --sky-bottom:#9fbcd0;
  --footer-top:#3f86b3;
  --footer-bottom:#17507e;
  --bar:#5b88a8;
  --white:#ffffff;
  --body:"Source Sans 3",sans-serif;
}
*{box-sizing:border-box;margin:0;padding:0}
html,body{width:925px;height:1200px;overflow:hidden;background:var(--white);font-family:var(--body)}
.page{position:relative;width:925px;height:1200px;overflow:hidden}
.abs{position:absolute}

/* header */
.site-header{left:0;top:0;width:925px;height:122px;background:var(--white)}
.brand{left:92px;top:52px;display:flex;align-items:center;gap:8px}
.brand-dot{width:40px;height:40px;border-radius:50%;background:var(--navy)}
.brand-name{font-size:27px;font-weight:600;color:var(--navy);letter-spacing:-0.5px;line-height:1}
.lang{left:590px;top:31px;display:flex;align-items:center;gap:8px;font-size:11px;color:#111}
.lang-select{width:122px;height:21px;border:1px solid #555;border-radius:2px;display:flex;align-items:center;justify-content:space-between;padding-left:5px;font-size:11px}
.lang-arrow{width:21px;height:19px;background:#111;display:flex;align-items:center;justify-content:center}
.main-nav{left:484px;top:79px;display:flex;gap:1px}
.main-nav a{width:87px;height:24px;display:flex;align-items:center;justify-content:center;font-size:10px;color:#bbb;text-decoration:none;background:linear-gradient(#3b3b3b,#111);border-radius:3px 3px 0 0;transform:skewX(-6deg)}
.main-nav a.active{background:linear-gradient(#3a84bd,#14507f);color:var(--white)}
.header-rule{left:0;top:121px;width:925px;height:3px;background:linear-gradient(#c9a0a8,#5a3a44)}

/* hero */
.hero{left:0;top:124px;width:925px;height:263px;background:var(--dark)}
.hero-photo{left:9px;top:11px;width:907px;height:202px;background:linear-gradient(#e89aa0 0%,#e48c86 45%,#b4603e 65%,#3a2a30 88%,#6a6a78 100%)}
.hero-arrow{top:94px;width:20px;height:20px;background:#111;display:flex;align-items:center;justify-content:center}
.hero-controls{left:756px;top:226px;display:flex;gap:3px;align-items:center}
.hero-controls span{width:18px;height:18px;background:#eee;display:flex;align-items:center;justify-content:center}
.hero-controls span.play{width:22px;height:22px}
.hero-shadow{left:100px;top:387px;width:720px;height:18px;background:radial-gradient(ellipse at top,rgba(0,0,0,.45),rgba(0,0,0,0) 70%)}

/* services */
.services{left:0;top:387px;width:925px;height:378px;background:linear-gradient(var(--sky-top),var(--sky-bottom));z-index:-1}
.service-frame{top:419px;width:242px;height:194px;background:var(--panel);padding:8px}
.service-frame div{width:100%;height:100%}
.service-card{top:620px;width:240px;height:112px;background:var(--panel);color:var(--panel-text);padding:6px 7px;box-shadow:0 6px 6px -3px rgba(0,0,0,.35)}
.service-card h2{font-size:15px;font-weight:400;color:var(--white);text-align:center;padding-bottom:5px;border-bottom:1px solid #555;margin:0 18px 9px}
.service-card p{font-size:10px;line-height:15.5px}

/* message */
.message{left:0;top:765px;width:925px;height:193px;background:#242424}
.message h2{left:92px;top:14px;font-size:19px;font-weight:700;color:var(--white)}
.message-field{left:92px;top:39px;width:371px;height:128px;background:#4d4d4d;border:2px solid #1a1a1a;padding:9px 6px;font-style:italic;font-size:10px;line-height:13px;color:#eee}
.message-button{left:493px;width:340px;height:48px;background:linear-gradient(#2f7db4,#0e3e68);border:1px solid #0a2f52;color:var(--white);font-size:23px;font-weight:600;letter-spacing:1px;display:flex;align-items:center;justify-content:center}

/* footer */
.site-footer{left:0;top:958px;width:925px;height:172px;background:linear-gradient(var(--footer-top),var(--footer-bottom));border-top:15px solid #8fb0c6;color:#dce8f2}
.footer-col{top:24px}
.footer-col h3{font-size:18px;font-weight:600;color:var(--white);margin-bottom:12px}
.contact-list li{list-style:none;font-size:10px;margin-bottom:12px}
.social-list li{list-style:none;display:flex;align-items:center;gap:10px;font-size:12.5px;margin-bottom:8px}
.social-dot{width:25px;height:25px;border-radius:50%;background:#1c5a8f;border:2px solid #cfe2f0}
.blog-list li{list-style:none;font-size:8.5px;line-height:12px;padding-left:10px;position:relative;margin-bottom:15px;width:160px}
.blog-list li::before{content:"";position:absolute;left:2px;top:4px;width:4px;height:4px;border-radius:50%;background:#dce8f2}
.partner-name{font-size:16px;font-weight:600;color:var(--navy)}
.partner-photo{width:76px;height:57px;margin-top:12px;background:linear-gradient(#eef2f5,#b8c3cc 60%,#2b2f36)}
.bottom-bar{left:0;top:1130px;width:925px;height:70px;background:var(--bar);border-top:1px solid #3b6686;font-size:13px;font-weight:600;color:#1b1b1b}
.bottom-bar span{color:var(--navy)}
</style>
</head>
<body>
<div class="page">
  <header class="site-header abs">
    <div class="brand abs"><span class="brand-dot"></span><span class="brand-name">Tidewell Marketing</span></div>
    <div class="lang abs">Choose language:
      <div class="lang-select">English<span class="lang-arrow"><svg width="9" height="8"><path d="M0 0h9L4.5 8z" fill="#fff"/></svg></span></div>
    </div>
    <nav class="main-nav abs">
      <a class="active" href="#">Offer</a><a href="#">About us</a><a href="#">Experience</a><a href="#">Contact</a>
    </nav>
  </header>
  <div class="header-rule abs"></div>

  <section class="hero abs">
    <div class="hero-photo abs" role="img" aria-label="Panoramic city skyline at sunset over the waterfront"></div>
    <span class="hero-arrow abs" style="left:93px"><svg width="8" height="10"><path d="M8 0v10L0 5z" fill="#fff"/></svg></span>
    <span class="hero-arrow abs" style="left:812px"><svg width="8" height="10"><path d="M0 0v10l8-5z" fill="#fff"/></svg></span>
    <div class="hero-controls abs">
      <span><svg width="4" height="6"><path d="M4 0v6L0 3z" fill="#000"/></svg></span>
      <span class="play"><svg width="7" height="9"><path d="M0 0v9l7-4.5z" fill="#000"/></svg></span>
      <span><svg width="4" height="6"><path d="M0 0v6l4-3z" fill="#000"/></svg></span>
    </div>
  </section>
  <div class="hero-shadow abs"></div>

  <section class="services abs"></section>
  <div class="service-frame abs" style="left:92px"><div role="img" aria-label="Magnifying glass over a printed bar chart" style="background:linear-gradient(135deg,#f1e6e2,#c9737c 55%,#4a4040)"></div></div>
  <div class="service-frame abs" style="left:342px"><div role="img" aria-label="Globe-patterned pie chart with an orange slice" style="background:radial-gradient(circle at 50% 55%,#3f7fd0 0%,#2d5fa8 35%,#f08a2a 36%,#ffffff 62%)"></div></div>
  <div class="service-frame abs" style="left:592px"><div role="img" aria-label="Bus shelter with an advertising poster on a city street" style="background:linear-gradient(90deg,#5ab6d8,#9fd6ea 40%,#b7b2a8 70%,#7c8a84)"></div></div>

  <article class="service-card abs" style="left:93px"><h2>Market Research</h2><p>Lorem Ipsum is simply dummy text of the printing and typesetting industry. Lorem Ipsum has been the industry's standard dummy text ever since the 1500s</p></article>
  <article class="service-card abs" style="left:343px"><h2>Marketing Plans</h2><p>Lorem Ipsum is simply dummy text of the printing and typesetting industry. Lorem Ipsum has been the industry's standard dummy text ever since the 1500s</p></article>
  <article class="service-card abs" style="left:593px"><h2>Marketing Project</h2><p>Lorem Ipsum is simply dummy text of the printing and typesetting industry. Lorem Ipsum has been the industry's standard dummy text ever since the 1500s</p></article>

  <section class="message abs">
    <h2 class="abs">MESSAGE</h2>
    <div class="message-field abs">Write your message and give details about<br>your company and activities.</div>
    <div class="message-button abs" style="top:40px">EMAIL</div>
    <div class="message-button abs" style="top:118px">SEND</div>
  </section>

  <footer class="site-footer abs">
    <div class="footer-col abs" style="left:92px">
      <h3>CONTACT</h3>
      <ul class="contact-list">
        <li>Phone: +XX - XXXXXXXXX</li><li>Fax: +XX - XXXXXXXXX</li>
        <li>Email: info@tidewellmarketing.com</li><li>Web: www.tidewellmarketing.com</li>
      </ul>
    </div>
    <div class="footer-col abs" style="left:282px">
      <h3>SOCIAL MEDIA</h3>
      <ul class="social-list">
        <li><span class="social-dot"></span>Circlebook</li>
        <li><span class="social-dot"></span>Linkwork</li>
        <li><span class="social-dot"></span>Chirper</li>
      </ul>
    </div>
    <div class="footer-col abs" style="left:463px">
      <h3>BLOG</h3>
      <ul class="blog-list">
        <li>Lorem Ipsum is simply dummy text of the printing and typesetting industry. Lorem Ipsum has been the industry's s</li>
        <li>Lorem Ipsum is simply dummy text of the printing and typesetting industry. Lorem Ipsum has been the industry's s</li>
      </ul>
    </div>
    <div class="footer-col abs" style="left:656px">
      <h3>PARTNERS</h3>
      <div class="partner-name">Tidewell Marketing</div>
      <div class="partner-photo" role="img" aria-label="Silhouettes of business people in front of a world map"></div>
    </div>
  </footer>
  <div class="bottom-bar abs">
    <div class="abs" style="left:92px;top:17px"><span>Tidewell</span> Marketing © 2012 All rights reserved.</div>
    <div class="abs" style="right:92px;top:17px">Created by: <span>Tidewell</span> Marketing</div>
  </div>
</div>
</body>
</html>
```